Business Card Design for Occupational Medicine Start Up Company

We need to design a professional business card. We are a healthcare company providing occupational medicine services to blue collar industries. We are professional, efficient and high quality service providers.

Target Market(s)

Blue Collar Industry: Shipbuilding, Ports, Trucking Companies; The Executives and Safety Officers for these companies

Industry/Entity Type

Healthcare

Contact Information for Business Card

Logo, Name, Title, Email, Phone

Other font styles liked:
• Please match our Brand Guide

Requirements
Must have
• Our Company Colors and Logo

```html
<!DOCTYPE html>
<html lang="en">
<head>
<meta charset="utf-8">
<title>Crewline Clinics – Business Card</title>
<link href="https://fonts.googleapis.com/css2?family=Montserrat:wght@400;500;600&display=swap" rel="stylesheet">
<style>
  :root {
    --navy: #232a77;
    --sky: #22abe5;
    --paper: #ffffff;
    --mist-top: #e4e4e7;
    --mist-bottom: #f4f4f5;
    --backdrop: #e3e6e7;
  }
  html, body {
    margin: 0;
    padding: 0;
    width: 1200px;
    height: 800px;
    overflow: hidden;
    background: var(--backdrop);
    font-family: "Montserrat", Arial, sans-serif;
  }
  .canvas {
    position: relative;
    width: 1200px;
    height: 800px;
  }
  .card {
    position: absolute;
    overflow: hidden;
    box-shadow: 0 1px 3px rgba(0,0,0,0.12);
  }

  /* Front */
  .card-front {
    left: 193px;
    top: 101px;
    width: 431px;
    height: 270px;
    background: var(--sky);
  }
  .front-top {
    position: absolute;
    left: 0; top: 0;
    width: 100%;
    height: 123px;
    background: linear-gradient(180deg, var(--mist-top), var(--mist-bottom));
  }
  .brand {
    position: absolute;
    display: flex;
    align-items: center;
    gap: 8px;
    color: var(--navy);
    font-weight: 600;
    text-transform: uppercase;
    white-space: nowrap;
  }
  .brand-dot {
    border-radius: 50%;
    background: var(--navy);
    flex: none;
  }
  .front-brand {
    left: 20px;
    top: 28px;
    font-size: 13px;
    letter-spacing: 0.06em;
  }
  .front-brand .brand-dot { width: 26px; height: 26px; }

  .name-band {
    position: absolute;
    left: 0;
    top: 81px;
    width: 241px;
    height: 62px;
  }
  .holder-name {
    position: absolute;
    left: 27px;
    top: 100px;
    margin: 0;
    color: var(--paper);
    font-size: 16px;
    font-weight: 500;
    letter-spacing: 0.04em;
  }
  .holder-role {
    position: absolute;
    left: 247px;
    top: 104px;
    margin: 0;
    color: var(--navy);
    font-size: 12px;
    font-weight: 400;
    letter-spacing: 0.05em;
  }
  .contact-list {
    position: absolute;
    left: 27px;
    top: 160px;
    margin: 0;
    padding: 0;
    list-style: none;
  }
  .contact-item {
    display: flex;
    align-items: center;
    gap: 7px;
    height: 13px;
    margin-bottom: 10.5px;
    color: var(--paper);
    font-size: 8.5px;
    font-weight: 400;
    letter-spacing: 0.02em;
  }
  .contact-icon {
    width: 13px;
    height: 13px;
    flex: none;
  }
  .front-emblem {
    position: absolute;
    left: 320px;
    top: 155px;
    width: 90px;
    height: 90px;
    border: 5px solid var(--paper);
    border-radius: 50%;
    box-sizing: border-box;
  }

  /* Back */
  .card-back {
    left: 567px;
    top: 423px;
    width: 441px;
    height: 276px;
    background: var(--paper);
  }
  .back-stripe {
    position: absolute;
    left: 0;
    top: 124px;
    width: 16px;
    height: 152px;
    background: var(--sky);
  }
  .back-brand {
    left: 110px;
    top: 183px;
    font-size: 19px;
    letter-spacing: 0.05em;
    gap: 12px;
  }
  .back-brand .brand-dot { width: 40px; height: 40px; }
</style>
</head>
<body>
<main class="canvas">

  <section class="card card-front" aria-label="Business card front">
    <div class="front-top"></div>

    <div class="brand front-brand">
      <span class="brand-dot"></span>
      <span class="brand-name">Crewline Clinics</span>
    </div>

    <svg class="name-band" viewBox="0 0 241 62" aria-hidden="true">
      <path d="M0 0 H212 Q218 0 220 5 L240 52 Q243 62 233 62 H0 Z" fill="var(--navy)"/>
    </svg>
    <h1 class="holder-name">NAME SURNAME</h1>
    <p class="holder-role">POSITION</p>

    <ul class="contact-list">
      <li class="contact-item">
        <svg class="contact-icon" viewBox="0 0 13 13" aria-hidden="true">
          <rect width="13" height="13" rx="2" fill="var(--paper)"/>
          <path d="M4 3.2 L5.3 3 L6 4.8 L5.2 5.5 Q5.8 7 7.5 7.8 L8.2 7 L10 7.7 L9.8 9 Q9.5 9.8 8.5 9.7 Q4.5 9 3.3 4.5 Q3.2 3.5 4 3.2 Z" fill="var(--sky)"/>
        </svg>
        <span>+012 34567890</span>
      </li>
      <li class="contact-item">
        <svg class="contact-icon" viewBox="0 0 13 13" aria-hidden="true">
          <rect width="13" height="13" rx="2" fill="var(--paper)"/>
          <rect x="3" y="4" width="7" height="5" fill="none" stroke="var(--sky)" stroke-width="0.9"/>
          <path d="M3 4 L6.5 6.8 L10 4" fill="none" stroke="var(--sky)" stroke-width="0.9"/>
        </svg>
        <span>email@yourcompany.com</span>
      </li>
      <li class="contact-item">
        <svg class="contact-icon" viewBox="0 0 13 13" aria-hidden="true">
          <rect width="13" height="13" rx="2" fill="var(--paper)"/>
          <path d="M6.5 10.5 Q3.8 7.3 3.8 5.4 A2.7 2.7 0 0 1 9.2 5.4 Q9.2 7.3 6.5 10.5 Z" fill="var(--sky)"/>
          <circle cx="6.5" cy="5.4" r="1" fill="var(--paper)"/>
        </svg>
        <span>Company street</span>
      </li>
      <li class="contact-item">
        <svg class="contact-icon" viewBox="0 0 13 13" aria-hidden="true">
          <rect width="13" height="13" rx="2" fill="var(--paper)"/>
          <g fill="none" stroke="var(--sky)" stroke-width="0.8">
            <circle cx="6.5" cy="6.5" r="3.4"/>
            <ellipse cx="6.5" cy="6.5" rx="1.5" ry="3.4"/>
            <path d="M3.1 6.5 H9.9"/>
          </g>
        </svg>
        <span>www.companywebsite.com</span>
      </li>
    </ul>

    <div class="front-emblem" aria-hidden="true"></div>
  </section>

  <section class="card card-back" aria-label="Business card back">
    <div class="back-stripe"></div>
    <div class="brand back-brand">
      <span class="brand-dot"></span>
      <span class="brand-name">Crewline Clinics</span>
    </div>
  </section>

</main>
</body>
</html>
```